Folderdesign für Hundeshop und Hundesalon Paw Lumo
Zielgruppe
Hundesalon ( paw-lumo.de)
Hundeshop mit Onlineshop (hundeshop-paw-lumo.de)
Zielgruppe: Hundebesitzer
Aufgabenstellung
Das Design sollte klar strukturiert und keinesfalls überladen sein, sondern mit einem Blick gut zu erfassen sein, farblich passend zu Naturkauartikeln, Kauartikeln ohne chem. Zusatzstoffe,...s Homepage
Erste Seite soll Hundesalon UND Hundeshop bewerben
Hervorgehoben werden soll der Hundeshop, da er als Onlineshop neu ist. Die Informationen entnehmen Sie bitte der HP www.hundeshop-paw-lumo.de.
Der Hundesalon soll eine Seite bekommen
DIN A 4 Wickelfalz, 6seitig...lasse mich aber gerne beraten falls jemand etwas anderes besser findet
Habe schon mal einen Flyer entworfen, aber er sieht mir zu normal und einfach aus. Texte können auch gerne verändert werden

```html
<!DOCTYPE html>
<html lang="de">
<head>
<meta charset="utf-8">
<title>Hundeshop Paw Lumo – Folder Innenseite</title>
<link rel="stylesheet" href="https://fonts.googleapis.com/css2?family=Ubuntu:wght@400;500;700&family=Pinyon+Script&display=swap">
<style>
  :root {
    --green: #8cc43f;
    --green-light: #a3d15a;
    --green-dark: #6fa82c;
    --green-text: #72ad2f;
    --white: #ffffff;
    --paper: #f7f8f6;
    --shade: #d9dcd6;
    --sans: "Ubuntu", "Open Sans", sans-serif;
    --script: "Pinyon Script", cursive;
  }
  * { box-sizing: border-box; margin: 0; padding: 0; }
  html, body { width: 1200px; height: 800px; overflow: hidden; background: #ececec; }
  .spread { position: relative; width: 1200px; height: 800px; font-family: var(--sans); }
  .panel { position: absolute; top: 0; width: 400px; height: 800px; }
  .panel--collars { left: 0; background: linear-gradient(160deg, var(--green-light), var(--green) 55%, var(--green-dark)); }
  .panel--shop { left: 400px; background: var(--paper); }
  .panel--barf { left: 800px; background: linear-gradient(200deg, var(--green-light), var(--green) 55%, var(--green-dark)); }

  .waves { position: absolute; inset: 0; width: 1200px; height: 800px; }

  .content { position: absolute; z-index: 2; }
  .title { color: var(--white); font-weight: 500; font-size: 24px; letter-spacing: 1px; }
  .script { font-family: var(--script); font-weight: 400; }

  /* left panel */
  .collars-head { left: 40px; top: 56px; }
  .collars-head .script { color: #e9f5d8; font-size: 24px; margin-top: 8px; }
  .features { list-style: none; }
  .features li { position: relative; padding-left: 20px; }
  .features li::before {
    content: ""; position: absolute; left: 2px; top: 0.45em;
    width: 8px; height: 8px; border-radius: 50%; background: currentColor;
  }
  .collars-list { left: 42px; top: 150px; color: var(--white); font-size: 14px; line-height: 20px; }

  .photo {
    position: absolute; border-radius: 50%; border: 5px solid var(--white);
    box-shadow: 0 4px 10px rgba(0,0,0,.25);
  }
  .photo--collar-red { left: 40px; top: 355px; width: 210px; height: 135px; background: radial-gradient(circle at 45% 50%, #8d1f25, #3a1a16 55%, #d8d2c8 85%); z-index: 2; }
  .photo--collar-bright { left: 180px; top: 455px; width: 210px; height: 135px; background: radial-gradient(circle at 55% 60%, #5a3a2a, #e44a9a 45%, #b8e04a 65%, #f2e44a 80%, #e8e4dc); z-index: 3; }

  .kiosk-note { left: 50px; top: 650px; color: var(--white); font-size: 16px; line-height: 19px; width: 320px; }
  .kiosk-note p + p { margin-top: 16px; }

  /* middle panel */
  .shop-head { left: 400px; top: 30px; width: 400px; text-align: center; color: var(--green-text); }
  .shop-name { font-size: 62px; line-height: 1.1; }
  .shop-tagline { font-size: 18px; line-height: 22px; letter-spacing: .5px; margin-top: 2px; }
  .shop-intro { font-size: 27px; line-height: 34px; margin-top: 26px; }

  .swoosh { position: absolute; left: 450px; top: 330px; width: 300px; height: 170px; border-radius: 50%; background: var(--green); z-index: 1; }
  .photo--treats { left: 470px; top: 315px; width: 290px; height: 170px; background: radial-gradient(ellipse at 50% 50%, #d9b48a, #b98a5a 50%, #6d5a4e 85%); z-index: 2; }

  .shop-list { left: 470px; top: 510px; color: var(--green-text); font-size: 16px; line-height: 21px; }

  .url { left: 400px; top: 728px; width: 400px; text-align: center; color: var(--white); font-size: 21px; font-weight: 500; letter-spacing: .5px; }

  /* right panel */
  .barf-head { left: 800px; top: 46px; width: 400px; text-align: center; color: var(--white); }
  .barf-head .script { font-size: 24px; margin-top: 6px; color: #eef8e0; }
  .barf-steps { left: 800px; top: 130px; width: 400px; text-align: center; color: var(--white); list-style: none; }
  .barf-steps li strong { display: block; font-weight: 500; font-size: 15px; line-height: 18px; }
  .barf-steps li strong::before { content: ""; display: inline-block; width: 7px; height: 7px; border-radius: 50%; background: var(--white); margin-right: 6px; vertical-align: middle; }
  .barf-steps li span { display: block; font-size: 11px; line-height: 13px; }
  .barf-steps .plus { font-size: 16px; line-height: 18px; }
  .barf-closing { left: 800px; top: 352px; width: 400px; text-align: center; color: var(--white); font-size: 30px; }

  .barf-arc { position: absolute; left: 845px; top: 430px; width: 310px; height: 185px; border-radius: 50%; background: var(--white); opacity: .55; z-index: 1; }
  .photo--dog { left: 855px; top: 415px; width: 300px; height: 180px; background: radial-gradient(ellipse at 50% 55%, #8a6a4a, #b89870 45%, #d6c6a8 80%); z-index: 2; }

  .footnote { left: 870px; top: 672px; width: 310px; color: var(--white); font-size: 15px; line-height: 18px; }
</style>
</head>
<body>
<main class="spread">
  <section class="panel panel--collars"></section>
  <section class="panel panel--shop"></section>
  <section class="panel panel--barf"></section>

  <svg class="waves" viewBox="0 0 1200 800" aria-hidden="true">
    <defs>
      <linearGradient id="bandGreen" x1="0" y1="0" x2="1" y2="1">
        <stop offset="0" stop-color="#a3d15a"/>
        <stop offset=".5" stop-color="#8cc43f"/>
        <stop offset="1" stop-color="#6fa82c"/>
      </linearGradient>
    </defs>
    <path d="M0,640 C300,600 500,720 800,680 C1000,654 1100,612 1200,600 L1200,800 L0,800 Z" fill="url(#bandGreen)"/>
    <path d="M0,636 C300,596 500,716 800,676 C1000,650 1100,608 1200,596" fill="none" stroke="#d9dcd6" stroke-width="22"/>
    <path d="M0,632 C300,592 500,712 800,672 C1000,646 1100,604 1200,592" fill="none" stroke="#ffffff" stroke-width="16"/>
  </svg>

  <!-- left panel -->
  <header class="content collars-head">
    <h2 class="title">Halsbänder und Leinen</h2>
    <p class="script">handgefertigt nach Ihren Wünschen</p>
  </header>
  <ul class="content features collars-list">
    <li>extrem reißfest</li>
    <li>sehr leicht, daher hoher Tragekomfort</li>
    <li>Farbe und Muster individuell kombinierbar</li>
    <li>ein, zwei- oder dreifarbig</li>
    <li>in 2cm, 3cm und 4cm Breite erhältlich</li>
    <li>wetterbeständig</li>
    <li>waschbar bei 30 °C</li>
    <li>verschiedene Verschlüsse möglich</li>
  </ul>
  <div class="photo photo--collar-red" role="img" aria-label="Foto: gewebtes rot-goldenes Hundehalsband"></div>
  <div class="photo photo--collar-bright" role="img" aria-label="Foto: geflochtene Halsbänder in Pink, Grün und Gelb"></div>
  <div class="content kiosk-note">
    <p>In unserem Hundekiosk können Sie alles auch in kleinsten Mengen bestellen!</p>
    <p>Und natürlich erhalten Sie bei uns eine kostenlose Beratung!</p>
  </div>

  <!-- middle panel -->
  <header class="content shop-head">
    <h1 class="script shop-name">Hundeshop</h1>
    <p class="shop-tagline">… weil das Beste gerade gut<br>genug ist!</p>
    <p class="script shop-intro">Gesunde Kauartikel sowie<br>Belohnungshappen und<br>Hamburger aus reinem Fleisch</p>
  </header>
  <div class="swoosh"></div>
  <div class="photo photo--treats" role="img" aria-label="Foto: Hundekekse in Knochenform und Kauartikel"></div>
  <ul class="content features shop-list">
    <li>ohne Konservierungsstoffe</li>
    <li>ohne Zucker</li>
    <li>ohne chemische Zusätze</li>
    <li>ohne Geschmacksverstärker</li>
    <li>gesund und fettarm</li>
    <li>selber mischen</li>
  </ul>
  <p class="content url">www.hundeshop-paw-lumo.de</p>

  <!-- right panel -->
  <header class="content barf-head">
    <h2 class="title">Nahrungsergänzung*</h2>
    <p class="script">so einfach ist barfen:</p>
  </header>
  <ul class="content barf-steps">
    <li><strong>Pures Fleisch</strong><span>vom Rind, Lamm, Geflügel, Wild, …</span></li>
    <li class="plus">+</li>
    <li><strong>Hochwertige Öle</strong><span>reich an Vitaminen und Omega-3-Fettsäuren</span></li>
    <li class="plus">+</li>
    <li><strong>Obst &amp; Gemüse</strong><span>tiefgefroren sowie Flockenmischungen</span></li>
    <li class="plus">+</li>
    <li><strong>Nahrungsergänzung</strong><span>bei Bedarf oder kurweise</span></li>
  </ul>
  <p class="content script barf-closing">Fertig ist die gesunde Mahlzeit !</p>
  <div class="barf-arc"></div>
  <div class="photo photo--dog" role="img" aria-label="Foto: kleiner Hund in Nahaufnahme"></div>
  <p class="content footnote">* BARF: Biologisch artgerechte Rohfütterung<br>Füttern von rohem Fleisch</p>
</main>
</body>
</html>
```